Flyer for the Lumen 2025 Conference

I am looking to produce a flyer for our upcoming conference, Lumen 2025. This is an annual conference that we plan to publicize on social media. The ideal designer will create a flyer that is eye-catching and effectively communicates the key information. Please see attached our logo, speaker photo, and flyer content.

Target Market(s)

All demographics

Industry/Entity Type

Christian

Font styles to use
Sans Serif

Requirements
Should not have
• Cross, church

```html
<!DOCTYPE html>
<html lang="en">
<head>
<meta charset="utf-8">
<title>Lumen 2025 Conference Flyer</title>
<link rel="stylesheet" href="https://fonts.googleapis.com/css2?family=Montserrat:wght@700;800&family=Great+Vibes&family=Bebas+Neue&family=Arimo:wght@400&display=swap">
<style>
  :root {
    --page: #ffffff;
    --night: #0c1430;
    --night-mid: #1b2a5c;
    --nebula: #5a3a6a;
    --gold: #e9b84a;
    --gold-light: #ffe08a;
    --cyan: #9fe6ff;
    --cyan-glow: #2fb7ff;
    --white: #f4f6fb;
  }
  * { margin: 0; padding: 0; box-sizing: border-box; }
  html, body { width: 1200px; height: 900px; overflow: hidden; background: var(--page); }
  .flyer {
    position: absolute; left: 240px; top: 90px; width: 720px; height: 720px; overflow: hidden;
    background:
      radial-gradient(circle at 50% 42%, rgba(255,214,140,0.55) 0, rgba(230,140,90,0.25) 12%, transparent 30%),
      radial-gradient(ellipse at 35% 35%, rgba(140,80,120,0.35), transparent 45%),
      radial-gradient(ellipse at 50% 50%, var(--night-mid), var(--night) 75%);
    font-family: "Arimo", Arial, sans-serif; color: var(--white);
  }
  .frame {
    position: absolute; left: 41px; top: 41px; width: 640px; height: 642px;
    border: 5px solid var(--gold-light);
    box-shadow: 0 0 14px 3px rgba(255,200,90,0.75), inset 0 0 14px 3px rgba(255,200,90,0.6);
  }
  .brand-mark {
    position: absolute; left: 0; right: 0; top: 52px; display: flex; justify-content: center; align-items: center; gap: 10px;
    font-family: "Montserrat", sans-serif; font-weight: 800; font-size: 30px; color: var(--gold); letter-spacing: 3px;
  }
  .brand-mark .dot { width: 22px; height: 22px; border-radius: 50%; background: var(--gold); }
  .event-name {
    position: absolute; left: 0; right: 0; top: 155px; text-align: center;
    font-family: "Montserrat", sans-serif; font-weight: 800; font-size: 43px; color: var(--gold); letter-spacing: 1px;
  }
  .event-tagline {
    position: absolute; left: 0; right: 0; top: 203px; text-align: center;
    font-family: "Great Vibes", cursive; font-size: 32px; color: var(--white);
  }
  .theme {
    position: absolute; left: 0; right: 0; top: 258px; text-align: center;
    font-family: "Bebas Neue", sans-serif; font-size: 70px; line-height: 1; letter-spacing: 2px; color: var(--cyan);
    text-shadow: 0 0 8px var(--cyan-glow), 0 0 18px rgba(47,183,255,0.6);
  }
  .soundline {
    position: absolute; left: 153px; top: 330px; width: 416px; height: 16px;
    background: linear-gradient(90deg, transparent, rgba(255,230,180,0.9) 50%, transparent);
    border-radius: 8px; opacity: 0.8;
  }
  .speaker-photo {
    position: absolute; left: 281px; top: 350px; width: 162px; height: 162px; border-radius: 50%;
    border: 3px solid var(--gold);
    background: radial-gradient(circle at 50% 40%, #3a3a40, #0d0d12 70%), #111;
  }
  .speaker-photo::after {
    content: ""; position: absolute; left: 22%; right: 22%; bottom: 0; height: 38%;
    border-radius: 50% 50% 0 0; background: linear-gradient(#2a6fd6, #1a4fa8);
  }
  .speaker-name { position: absolute; left: 0; right: 0; top: 530px; text-align: center; font-size: 15px; }
  .heading {
    position: absolute; font-family: "Montserrat", sans-serif; font-weight: 700; font-size: 15px; color: var(--gold);
  }
  .heading.schedule-title { left: 103px; top: 462px; }
  .heading.venue-title { left: 494px; top: 462px; width: 120px; text-align: center; }
  .schedule { position: absolute; left: 76px; top: 489px; list-style: none; font-size: 12px; line-height: 16px; }
  .schedule li::before { content: "•"; margin-right: 6px; }
  .venue { position: absolute; left: 474px; top: 482px; width: 160px; text-align: center; font-size: 14px; line-height: 16px; }
  .app-note { position: absolute; left: 0; right: 0; top: 594px; padding-left: 28px; text-align: center; font-size: 15px; }
  .phone {
    position: absolute; left: 336px; top: 618px; width: 55px; height: 93px; border-radius: 8px;
    border: 2px solid var(--gold); background: #14306a; display: flex; align-items: center; justify-content: center;
    font-family: "Arimo", sans-serif; font-size: 12px; color: var(--white);
  }
  .phone::before {
    content: ""; position: absolute; top: 4px; left: 20px; width: 15px; height: 3px; border-radius: 2px; background: var(--gold);
  }
  .contact { position: absolute; right: 410px; top: 653px; text-align: right; font-size: 12.5px; line-height: 15px; }
  .website { position: absolute; left: 410px; top: 663px; font-size: 12.5px; }
</style>
</head>
<body>
  <main class="flyer">
    <div class="frame"></div>

    <div class="brand-mark"><span class="dot"></span>LUMEN</div>
    <h1 class="event-name">LUMEN 2025</h1>
    <p class="event-tagline">A Prophetic Conference</p>
    <h2 class="theme">THE VOICE OF THE LORD</h2>
    <div class="soundline" role="img" aria-label="Glowing sound wave line"></div>

    <div class="speaker-photo" role="img" aria-label="Portrait of the guest speaker in a blue suit"></div>
    <p class="speaker-name">Prophet Elias Marron</p>

    <h3 class="heading schedule-title">DATE/TIME</h3>
    <ul class="schedule">
      <li>Friday, December 26th</li>
      <li>Friday, December 27 5:00PM - 9:00PM</li>
      <li>Saturday 27&nbsp;&nbsp;&nbsp;&nbsp;&nbsp;5:30PM - 8:00PM</li>
      <li>Sunday 29&nbsp;&nbsp;5:30PM - 8:00PM</li>
      <li>Monday 29&nbsp;&nbsp;4:30PM - 7:00PM</li>
    </ul>

    <h3 class="heading venue-title">LOCATION</h3>
    <address class="venue" style="font-style:normal">
      The Millbrook<br>Performing Arts Center<br>118 Alder Lane<br>Millbrook, Maine 04000
    </address>

    <p class="app-note">Download the HALEO App to stay updated on the event</p>
    <div class="phone">HALEO</div>
    <p class="contact">555 014 2387<br>contact@haleo.org</p>
    <p class="website">www.haleo.org</p>
  </main>
</body>
</html>
```